Landing Page for a new, High Production, farming technology

Brightfield Yield
We need a single landing page, with an email signup for more information.
We build self-contained, farming boxes out of ISO containers. These containers use hydroponics and LED lighting to provide a year round growing environment for crops. So, you could grow crops anywhere at any time of the year in any environment.
For the purpose of this site, we will be doing split testing between several different themes using different sites and keywords.
This site's focus should be providing our product to people searching for high production farming technology.
We'll be focusing on the following key words: Agriculture, aquaponics, farm, garden, hydroponics, organic food, subsistence farming, urban farming, vertical garden.
Target Market(s)
We are going to be using this page to judge that
Number of Pages Required
1 page
Look and feel
Each slider illustrates characteristics of the customer's brand and the style your logo design should communicate.

```html
<!DOCTYPE html>
<html lang="en">
<head>
<meta charset="utf-8">
<title>Brightfield Yield — High Production Farming Technology</title>
<link href="https://fonts.googleapis.com/css2?family=Poppins:wght@400;500;600&family=Open+Sans:wght@400;600&display=swap" rel="stylesheet">
<style>
:root{
  --orange:#eaa86c;
  --orange-deep:#e39a55;
  --green:#5f9f73;
  --green-band:#65a57a;
  --green-text:#4f9a66;
  --ink:#2d2d2d;
  --body:#555;
  --footer:#3b3b3b;
  --white:#fff;
}
*{margin:0;padding:0;box-sizing:border-box}
html,body{width:1200px;height:3109px;overflow:hidden}
body{position:relative;background:var(--white);font-family:"Open Sans",Arial,sans-serif;color:var(--body)}
.abs{position:absolute}
.heading{font-family:"Poppins",Arial,sans-serif;font-weight:500;color:var(--ink);text-transform:uppercase}
.label{font-family:"Poppins",Arial,sans-serif;font-size:11px;font-weight:500;color:var(--green-text);text-transform:uppercase;letter-spacing:.5px}
.copy{font-size:10px;line-height:16px}
.center{text-align:center;left:0;right:0}

/* header */
.site-header{left:0;top:0;width:1200px;height:93px;background:var(--orange)}
.brand{left:213px;top:24px;display:flex;align-items:center;gap:12px;color:var(--white);font-family:"Poppins",Arial,sans-serif}
.brand-mark{width:30px;height:30px;border:2px solid var(--white)}
.brand-name{font-size:15px;letter-spacing:5px;font-weight:500;line-height:1.2}
.brand-name small{display:block;font-size:8px;letter-spacing:2px;border-top:1px solid var(--white);padding-top:2px;text-align:center}
.nav{top:36px;font-family:"Poppins",Arial,sans-serif;font-size:11.5px;color:var(--white)}
.nav.active{border-bottom:2px solid var(--ink);padding-bottom:3px;color:var(--ink)}
.header-signup{left:879px;top:32px;width:110px;height:29px;border:1.5px solid var(--white);border-radius:6px;color:var(--white);font-family:"Poppins",Arial,sans-serif;font-size:11.5px;display:flex;align-items:center;justify-content:center}

/* hero */
.hero{left:0;top:93px;width:1200px;height:581px;background:radial-gradient(ellipse at 52% 60%,#9b8a5c 0%,#6f7a50 22%,#a9a9a2 48%,#d2d2d0 80%)}
.hero-title{top:308px;font-family:"Poppins",Arial,sans-serif;font-size:44px;font-weight:500;color:var(--white);letter-spacing:7px}
.hero-sub{top:363px;font-family:"Poppins",Arial,sans-serif;font-size:12px;color:var(--white);letter-spacing:14px}

/* products */
.products-title{top:785px;font-size:25px}
.products-intro{top:832px;left:310px;width:580px;text-align:center}
.product-photo{left:0;top:935px;width:593px;height:406px;background:linear-gradient(135deg,#2e3a3c 0%,#6f8e6a 35%,#a6c96c 55%,#3d4a4b 100%)}
.product-name{left:628px;width:357px;top:982px;text-align:center;font-family:"Poppins",Arial,sans-serif;font-size:17px;font-weight:500;color:var(--green-text)}
.feature-list{left:628px;top:1036px;width:357px;list-style:none}
.feature-list li{display:flex;gap:10px;padding:0 0 16px;margin-bottom:16px;border-bottom:1px solid #ddd;font-size:9.5px;line-height:13px;height:48px}
.feature-list li:last-child{border:none}
.tick{flex:0 0 12px;height:12px;margin-top:1px;background:var(--orange-deep);border-radius:2px}
.slider-btn{top:1316px;width:25px;height:25px;border-radius:5px;background:var(--ink)}
.cta{left:518px;top:1408px;width:162px;height:37px;background:var(--green);border-radius:5px;color:var(--white);font-family:"Poppins",Arial,sans-serif;font-size:11.5px;display:flex;align-items:center;justify-content:center}

/* about */
.about-panel{left:0;top:1544px;width:601px;height:498px;background:var(--orange)}
.about-photo{left:601px;top:1544px;width:599px;height:498px;background:linear-gradient(160deg,#b7b9a6 0%,#39507a 35%,#6f9e3e 65%,#b7d873 100%)}
.about-label{left:213px;top:1684px}
.about-title{left:213px;top:1702px;font-size:24px;line-height:30px}
.about-text{left:213px;top:1790px;width:352px;color:var(--white);font-size:11px;line-height:20px;opacity:.95}

/* solutions */
.solutions-label{top:2132px}
.solutions-title{top:2152px;font-size:24px;line-height:30px}
.solutions-intro{top:2233px;left:280px;width:640px;text-align:center}
.solution{width:340px}
.solution svg{position:absolute;left:-56px;top:2px}
.solution h3{font-family:"Poppins",Arial,sans-serif;font-size:15px;font-weight:500;color:var(--green-text);margin-bottom:6px}

/* signup band */
.signup-band{left:0;top:2595px;width:1200px;height:313px;background:var(--green-band)}
.signup-title{top:2677px;font-family:"Poppins",Arial,sans-serif;font-size:24px;font-weight:500;color:var(--white);letter-spacing:2px}
.signup-text{top:2722px;left:310px;width:580px;text-align:center;color:var(--white)}
.email-input{left:390px;top:2807px;width:315px;height:37px;border:1.5px solid var(--white);border-radius:6px;color:var(--white);font-size:11px;font-style:italic;display:flex;align-items:center;padding-left:14px}
.submit{left:717px;top:2807px;width:96px;height:37px;border:1.5px solid var(--white);border-radius:6px;color:var(--white);font-size:11px;display:flex;align-items:center;justify-content:center}

/* footer */
.site-footer{left:0;top:2908px;width:1200px;height:201px;background:var(--footer);color:#ddd}
.footer-col{color:#ddd}
.footer-col h4{font-family:"Poppins",Arial,sans-serif;font-size:10.5px;font-weight:500;color:var(--white);padding-bottom:6px;border-bottom:1px solid #777;width:96px;margin-bottom:10px}
.footer-col p{font-size:8.5px;line-height:13px}
.footer-about{left:213px;top:2988px;width:190px;font-size:8.5px;line-height:12.5px;color:#ddd}
.copyright{left:213px;top:3084px;font-size:8.5px;color:#ddd}
.social{top:3083px;width:12px;height:12px;border-radius:2px;background:#ddd}
</style>
</head>
<body>

<header class="abs site-header">
  <div class="abs brand"><span class="brand-mark"></span><span class="brand-name">BRIGHTFIELD<small>YIELD</small></span></div>
  <span class="abs nav active" style="left:474px">Home</span>
  <span class="abs nav" style="left:541px">Products</span>
  <span class="abs nav" style="left:627px">About Us</span>
  <span class="abs nav" style="left:714px">Solutions</span>
  <span class="abs nav" style="left:799px">Contact</span>
  <span class="abs header-signup">Sign Up</span>
</header>

<section class="abs hero" role="img" aria-label="Close-up photo of seedlings sprouting from a growing cube"></section>
<h1 class="abs center hero-title">THE NEW WAY OF FARMING</h1>
<p class="abs center hero-sub">HIGH PRODUCTION FARMING TECHNOLOGY</p>

<p class="abs center label" style="top:765px">Our Products</p>
<h2 class="abs center heading products-title">High Production Farming Technology</h2>
<p class="abs copy products-intro">Lorem ipsum dolor sit amet, consectetur adipiscing elit. Proin gravida nibh vel velit auctor aliquet. Aenean sollicitudin, lorem quis bibendum auctor, nisi elit consequat ipsum, nec sagittis sem nibh id elit. Duis sed odio sit amet nibh vulputate cursus a sit</p>

<div class="abs product-photo" role="img" aria-label="Photo of vertical hydroponic racks with LED-lit greens inside a container"></div>
<h3 class="abs product-name">GROWING BOX ONE</h3>
<ul class="abs feature-list">
  <li><span class="tick"></span><span>Lorem ipsum dolor sit amet, consectetur elit. Proin gravida nibh vel velit auctor aliquet. Aenean sollicitudin, lorem quis bibendum auctor, nisi elit</span></li>
  <li><span class="tick"></span><span>Lorem ipsum dolor sit amet, consectetur elit. Proin gravida nibh vel velit auctor aliquet. Aenean sollicitudin, lorem quis bibendum auctor, nisi elit</span></li>
  <li><span class="tick"></span><span>Lorem ipsum dolor sit amet, consectetur elit. Proin gravida nibh vel velit auctor aliquet. Aenean sollicitudin, lorem quis bibendum auctor, nisi elit</span></li>
  <li><span class="tick"></span><span>Lorem ipsum dolor sit amet, consectetur elit. Proin gravida nibh vel velit auctor aliquet. Aenean sollicitudin, lorem quis bibendum auctor, nisi elit</span></li>
</ul>
<svg class="abs slider-btn" style="left:933px" viewBox="0 0 25 25"><path d="M14.5 8l-4.5 4.5 4.5 4.5" stroke="#fff" stroke-width="2" fill="none"/></svg>
<svg class="abs slider-btn" style="left:962px" viewBox="0 0 25 25"><path d="M10.5 8l4.5 4.5-4.5 4.5" stroke="#fff" stroke-width="2" fill="none"/></svg>
<a class="abs cta">Sign Up</a>

<section class="abs about-panel"></section>
<div class="abs about-photo" role="img" aria-label="Photo of a farmer in a straw hat tending lettuce in a greenhouse"></div>
<p class="abs label about-label">About Us</p>
<h2 class="abs heading about-title">Grow Crops Anywere<br>At Any Time of the Year</h2>
<p class="abs about-text">Lorem ipsum dolor sit amet, consectetur elit. Proin gravida nibh vel velit auctor aliquet. Aenean sollicitudin, lorem quis bibendum auctor, nisi elit consequat ipsum, nec sagittis sem nibh id elit. Duis sed odio sit amet nibh vulputate cursus a sit amet mauris. Morbi accumsan ipsum velit. Nam nec tellus a odio tincidunt auctor a ornare odio. Sed non mauris vitae erat consequat auctor eu in elit. Class aptent taciti sociosqu</p>

<p class="abs center label solutions-label">Solutions</p>
<h2 class="abs center heading solutions-title">We Provide Best Solutions for Customers,<br>Humanity &amp; the Environment</h2>
<p class="abs copy solutions-intro">Lorem ipsum dolor sit amet, consectetur elit. Proin gravida nibh vel velit auctor aliquet. Aenean sollicitudin, lorem quis bibendum auctor, nisi elit consequat ipsum, nec sagittis sem nibh id elit. Duis sed odio sit amet nibh vulputate cursus a sit amet mauris. Morbi accumsan</p>

<div class="abs solution" style="left:278px;top:2334px">
  <svg width="40" height="40" viewBox="0 0 40 40"><circle cx="20" cy="20" r="12" fill="none" stroke="#e39a55" stroke-width="5" stroke-dasharray="5 3.4"/><circle cx="20" cy="20" r="6" fill="#e39a55"/></svg>
  <h3>Innovative Systems</h3>
  <p class="copy">Lorem ipsum dolor sit amet, consectetur elit. Proin gravida nibh vel velit auctor aliquet. Aenean sollicitudin, lorem quis bibendum</p>
</div>
<div class="abs solution" style="left:670px;top:2334px">
  <svg width="40" height="40" viewBox="0 0 40 40"><circle cx="20" cy="17" r="10" fill="none" stroke="#e39a55" stroke-width="3"/><rect x="15" y="28" width="10" height="6" fill="#e39a55"/><path d="M20 11v8" stroke="#e39a55" stroke-width="3"/></svg>
  <h3>Intelligent Solutions</h3>
  <p class="copy">Lorem ipsum dolor sit amet, consectetur elit. Proin gravida nibh vel velit auctor aliquet. Aenean sollicitudin, lorem quis bibendum</p>
</div>
<div class="abs solution" style="left:278px;top:2456px">
  <svg width="40" height="40" viewBox="0 0 40 40"><path d="M6 20c0 8 6 14 14 14s14-6 14-14" fill="none" stroke="#e39a55" stroke-width="3"/><path d="M20 8c-6 2-8 8-6 14 6-1 8-7 6-14z" fill="#e39a55"/></svg>
  <h3>Friendly Environment</h3>
  <p class="copy">Lorem ipsum dolor sit amet, consectetur elit. Proin gravida nibh vel velit auctor aliquet. Aenean sollicitudin, lorem quis bibendum</p>
</div>
<div class="abs solution" style="left:670px;top:2456px">
  <svg width="40" height="40" viewBox="0 0 40 40"><path d="M8 32C8 16 18 8 34 6c-2 16-10 26-26 26z" fill="#e39a55"/><path d="M8 32L24 16" stroke="#fff" stroke-width="2"/></svg>
  <h3>Organic Food</h3>
  <p class="copy">Lorem ipsum dolor sit amet, consectetur elit. Proin gravida nibh vel velit auctor aliquet. Aenean sollicitudin, lorem quis bibendum</p>
</div>

<section class="abs signup-band"></section>
<h2 class="abs center signup-title">FIND MORE ABOUT OUR PRODUCTS</h2>
<p class="abs copy signup-text">Lorem ipsum dolor sit amet, consectetur adipiscing elit. Proin gravida nibh vel velit auctor aliquet. Aenean sollicitudin, lorem quis bibendum auctor, nisi elit consequat ipsum, nec sagittis sem nibh id elit. Duis sed odio sit amet nibh vulputate cursus a sit</p>
<div class="abs email-input">Enter your Email Address</div>
<div class="abs submit">Submit</div>

<footer class="abs site-footer"></footer>
<div class="abs brand" style="top:2936px"><span class="brand-mark"></span><span class="brand-name">BRIGHTFIELD<small>YIELD</small></span></div>
<p class="abs footer-about">Fresh greens grown in sealed boxes with smart light and water. Our farms run all year in any climate, close to the people who eat the crops, with less land, less water and no long trucks needed at all.</p>
<div class="abs footer-col" style="left:477px;top:2946px"><h4>COMPANY</h4><p>Home<br>Services<br>About Us</p></div>
<div class="abs footer-col" style="left:667px;top:2946px"><h4>PRODUCTS</h4><p>Lorem Ipsum<br>Lorem Ipsum Dolar<br>Lorem Ipsum</p></div>
<div class="abs footer-col" style="left:850px;top:2946px"><h4>CONTACT</h4><p>48 Meadow Lane,<br>Fairview, OR, USA<br>97024<br><br>hello@brightfieldyield.example<br>0800 555 014</p></div>
<p class="abs copyright">© 2018. Brightfield Yield. All Rights Reserved.</p>
<span class="abs social" style="left:938px"></span>
<span class="abs social" style="left:956px"></span>
<span class="abs social" style="left:974px"></span>

</body>
</html>
```